Wordpress Design Project

WHO WE ARE:
Bright Path Web Growth is not just another SEO or PPC company. We work with our clients to help them grow their business and achieve their goals. Our commitment to doing what is best for the customer, is why we have grown so quickly. We believe our business is not about advertising BUT about connecting customers & growing our clients businesses. We see our product as helping people, not selling a product.

PROJECT OVERVIEW:
I need to create a wordpress website for my business, www.brightpathwebgrowth.com.au

I need a whole new site created showing all of my services. The services include:
NOTE: These are not the main focus of the home page.

Consulting & Strategy Planning
Search Engine Optimisation
Pay Per Click
Re-Marketing

Once I have selected the top home page design, I will need a product and blog page designed.

SITE DESIGN:
If I was to explain the kind of style I am looking for, it would be high-street, New York agency look, web 2.0. Clean, elegant, stylish, high quality and simple looking. Kind of like you would expect from an quince website.

Think of car advertising, the closest to the target market & look/feel Im looking for would be Ravenmotor, Korel, Tamar, Brandin, Zepra.

However, I am open to any design style.

DO NOT let this restrict your creativity BUT here are some websites I like the look of.

Home page:
http://www.layoutfoundry.example/demo/52816.html
https://www.vantorix.example/intl/en/halo/devices/
http://www.vantorix.example/intl/en/halo/devices/features-different.html
http://www.layoutfoundry.example/demo/47190.html
https://www.vantorix.example/intl/en/halo/browser/features.html

Product Page:
http://www.vantorix.example/intl/en/halo/devices/buynow.html#instore

NOTE: I just added a file called "I like this color scheme.png" you can play around with something like this as well.
Updates

Please do not use the content from my current website. That is for a PPC service, the new site is for an full service agency.

Also, the message/tagline is the feature or most prominent element of the website..... Not the services we offer, these are secondary.

Great designs so far everyone, but I think I'm looking a little simpler and less crowded.  Closer to the sample sites I sent.... keep em coming.

Also, I would prefer that the 4 services, do not visually over power the tag line.  The 4 services are not important to the home page.

Lets make this easy, since every design I receive is almost the same...

Make the design look something like these 2 websites.
https://www.vantorix.example/intl/en/halo/browser/features.html#simplicity

Target Market(s)

Business Owners and entreprenuers who are well established, typically in the 35-60 year old range and spend 100k-1m in advertising per year. They big brands that target these people are Ravenmotor, Korel, Tamar, Brandin, Zepra, this should give you the feel for what I am after.

Industry/Entity Type

Advertising

Requirements
Must have
• 1. Navigations: Home, Services, About Us, Blog, Contact Us

2. The main home page words should be.... "We Grow Your Business Online" and "Clear Aim, Clear Plan, Clear Team, Bright Path Web Growth" (should use logo for last one)
I would like to see this tagline somewhere in the site "We Don't Want to be the Biggest, Just the Best!"

3. Product page must have a contact form with (name, email, phone, website)
This form must show an offer of "Free Strategy Sessions, Double your website leads", I have included an image to show as an example for the lead form "lead form example.png", see attached.

Nice to have
• I would like to see 1 or 2 of these idea's in the design.

1. I have attached some logos for Bidlane & Metricove certifications + Web association logo you can use for design purposes.

2. You can put company logo's in the design and I can change them to my clients logos at a later date.

3. Testimonials

4. Since our business is about people, pictures of people like business owners, customers using technology such as an slate, or anything like that would be good. However, is not necessary. Some idea: http://www.peerlattice.example/advertising
Should not have
• There will be no video on the design.

```html
<!DOCTYPE html>
<html lang="en">
<head>
<meta charset="utf-8">
<title>Bright Path Web Growth</title>
<link href="https://fonts.googleapis.com/css2?family=Source+Sans+3:ital,wght@0,400;0,600;0,700;1,400&display=swap" rel="stylesheet">
<style>
:root{
  --blue:#1b5fae;
  --blue-dark:#164e91;
  --ink:#333;
  --text:#444;
  --grey-bar:#c9c9c9;
  --grey-line:#cfcfcf;
  --yellow:#f6be16;
  --yellow-dark:#e3a70b;
  --footer:#b3b3b3;
}
*{box-sizing:border-box;margin:0;padding:0}
html,body{width:907px;height:1200px;overflow:hidden}
body{position:relative;background:#fff;font-family:"Source Sans 3",Arial,sans-serif;color:var(--text)}
.abs{position:absolute}

.site-header{left:0;top:0;width:907px;height:76px;background:linear-gradient(#fff,#f1f1f1)}
.brand{left:30px;top:20px;display:flex;align-items:center;gap:9px;white-space:nowrap}
.brand-mark{width:30px;height:30px;border-radius:50%;background:var(--blue);flex:none}
.brand-name{font-size:21px;font-weight:600;color:#555;letter-spacing:.2px}
.header-tagline{right:26px;top:24px;font-size:21px;color:var(--blue)}

.main-nav{left:0;top:76px;width:907px;height:33px;background:linear-gradient(#d9d9d9,#bdbdbd);border-top:1px solid #aaa}
.main-nav ul{list-style:none;display:flex;gap:20px;padding:10px 0 0 36px}
.main-nav a{font-size:11px;color:var(--blue);text-decoration:none}

.hero-photo{left:25px;top:140px;width:480px;height:335px;background:radial-gradient(ellipse at 40% 50%,#e6e3df 0%,#f2f1ef 45%,#fff 75%)}
.hero-headline{right:27px;top:168px;text-align:right;font-size:43px;line-height:52px;color:#2a2a2a;font-weight:400}
.hero-headline .accent{color:var(--blue)}
.hero-brand{right:27px;top:352px;display:flex;align-items:center;gap:8px;white-space:nowrap}
.hero-brand .brand-mark{width:34px;height:34px}
.hero-brand .brand-name{font-size:19px;color:#bbb;line-height:34px}
.btn-learn{left:680px;top:395px;width:200px;height:36px;background:linear-gradient(var(--yellow),var(--yellow-dark));color:#fff;font-size:20px;text-align:center;line-height:36px;box-shadow:0 1px 2px rgba(0,0,0,.3)}

.what-we-do{left:36px;top:566px;width:835px;height:175px;border:1px solid var(--grey-line);border-radius:6px}
.panel-tab{left:36px;top:566px;width:136px;height:20px;background:linear-gradient(90deg,#c7c7c7,#dadada);clip-path:polygon(0 0,88% 0,100% 100%,0 100%);border-radius:6px 0 0 0}
.panel-tab span{position:absolute;left:48px;top:3px;font-size:11px;color:#fff}
.panel-tab-mark{left:44px;top:554px;width:30px;height:30px;border-radius:50%;background:var(--blue);border:2px solid #fff}
.service{width:215px}
.service h3{font-size:12.5px;font-weight:400;color:var(--blue);line-height:14px}
.service p{font-size:10px;line-height:13px;color:#444;text-align:justify}
.service-icon{width:36px;height:36px}
.partner-badge{left:630px;top:592px;width:80px;height:72px;border-radius:4px;background:linear-gradient(#eee,#dcdcdc)}
.promise{right:48px;top:588px;text-align:right;font-size:20px;line-height:26px;color:var(--blue)}
.promise-strong{left:628px;top:668px;font-size:37px;font-weight:600;color:var(--blue-dark);letter-spacing:.5px}
.panel-more{left:736px;top:722px;width:135px;height:19px;background:linear-gradient(90deg,#d9d9d9,#c7c7c7);clip-path:polygon(10% 0,100% 0,100% 100%,0 100%);border-radius:0 0 6px 0;color:#fff;font-size:11px;padding:3px 0 0 36px}

.clients-title{left:36px;top:832px;display:flex;align-items:center;gap:10px;font-size:28px;color:var(--blue);font-weight:600}
.clients-title svg{width:28px;height:28px}
.testimonial{width:212px}
.testimonial h4{font-size:12px;font-weight:600;color:var(--blue);line-height:14px}
.testimonial .who{font-size:10.5px;color:#333;line-height:13px;margin-bottom:13px}
.testimonial p{font-size:10px;line-height:12.8px;font-style:italic;color:#333;text-align:justify}
.case h4{font-size:12px;font-weight:600;color:var(--blue);line-height:14px}
.case li{list-style:none;font-size:10px;line-height:12.6px;color:#333;white-space:nowrap}
.photo{background:#fff;padding:5px;box-shadow:0 1px 4px rgba(0,0,0,.35)}
.photo div{width:100%;height:100%}
.leader{stroke:#333;stroke-width:1;fill:none}
.btn-read{left:640px;top:1087px;width:148px;height:30px;background:linear-gradient(var(--yellow),var(--yellow-dark));color:#fff;font-size:11px;font-weight:600;line-height:30px;padding-left:18px;box-shadow:0 1px 2px rgba(0,0,0,.3)}
.btn-read-mark{left:620px;top:1077px;width:32px;height:32px;border-radius:50%;background:var(--blue);border:2px solid #fff}

.site-footer{left:0;top:1167px;width:907px;height:33px;background:var(--footer);color:#fff;font-size:10px;text-align:right;padding:13px 26px 0 0}
</style>
</head>
<body>

<header class="site-header abs">
  <div class="brand abs"><span class="brand-mark"></span><span class="brand-name">Bright Path Web Growth</span></div>
  <div class="header-tagline abs">We Grow Your Business Online</div>
</header>

<nav class="main-nav abs">
  <ul><li><a href="#">Home</a></li><li><a href="#">Services</a></li><li><a href="#">About Us</a></li><li><a href="#">Blog</a></li><li><a href="#">Contact Us</a></li></ul>
</nav>

<section class="hero">
  <div class="hero-photo abs" role="img" aria-label="Smiling businesswoman at a laptop with colleagues in a bright office"></div>
  <h1 class="hero-headline abs">Clear Aim, Clear Plan,<br>Clear Team,<br><span class="accent">Bright Path Web Growth</span></h1>
  <div class="hero-brand abs"><span class="brand-mark"></span><span class="brand-name">Bright Path Web Growth</span></div>
  <a class="btn-learn abs">Learn More</a>
</section>

<section>
  <div class="what-we-do abs"></div>
  <div class="panel-tab abs"><span>What We Do</span></div>
  <div class="panel-tab-mark abs"></div>

  <svg class="service-icon abs" style="left:46px;top:600px" viewBox="0 0 36 36"><circle cx="18" cy="15" r="11" fill="#f7c21a"/><rect x="13" y="25" width="10" height="7" rx="2" fill="#999"/></svg>
  <div class="service abs" style="left:98px;top:600px"><h3>Consulting &amp; Strategy Planning</h3><p>We will assist your business strategies and planning for better results.</p></div>

  <svg class="service-icon abs" style="left:46px;top:668px" viewBox="0 0 36 36"><path d="M6 16a12 12 0 0 1 22-6" stroke="#2a7fd0" stroke-width="5" fill="none"/><path d="M30 20a12 12 0 0 1-22 6" stroke="#3aa63a" stroke-width="5" fill="none"/><path d="M24 4l8 2-4 7z" fill="#2a7fd0"/><path d="M12 32l-8-2 4-7z" fill="#3aa63a"/></svg>
  <div class="service abs" style="left:98px;top:666px"><h3>Pay Per Click</h3><p>We will develop Pay-per-click marketing. So your business will be getting more easier, more cost-effective, and delivers stronger results.</p></div>

  <svg class="service-icon abs" style="left:330px;top:600px" viewBox="0 0 36 36"><circle cx="22" cy="13" r="10" fill="#e4eef8" stroke="#9bb" stroke-width="2"/><path d="M15 20L5 31" stroke="#d06a1c" stroke-width="5" stroke-linecap="round"/></svg>
  <div class="service abs" style="left:391px;top:598px"><h3>Search Engine Optimisation</h3><p>We will boost your business up in the first page of popular search engine.</p></div>

  <svg class="service-icon abs" style="left:332px;top:666px" viewBox="0 0 36 36"><path d="M3 10l22 -6v26L3 24z" fill="#ddd" stroke="#999"/><rect x="25" y="10" width="8" height="14" fill="#3aa63a"/><rect x="12" y="24" width="5" height="9" fill="#777"/></svg>
  <div class="service abs" style="left:391px;top:665px"><h3>Re-Marketing</h3><p>We will add more values to your business and re-marketing it for you to increase your revenue.</p></div>

  <div class="partner-badge abs" role="img" aria-label="Search advertising qualification badge"></div>
  <div class="promise abs">We Don't Want<br>to be<br>the Biggest</div>
  <div class="promise-strong abs">Just the Best !</div>
  <div class="panel-more abs">Learn More</div>
</section>

<section>
  <h2 class="clients-title abs"><svg viewBox="0 0 28 28"><rect x="2" y="7" width="24" height="17" fill="#eef3f8" stroke="#8aa"/><path d="M2 7l12 10 12-10" stroke="#8aa" fill="none"/></svg>What Our Clients Say</h2>

  <div class="testimonial abs" style="left:36px;top:880px">
    <h4>LEAPCUB.COM</h4><div class="who">Ivan Tollard - CEO</div>
    <p>We are have been using BrightPathWebGrowth for nearly two years and are very satisfied with the services they have provided and results achieved in both SEO and PPC. They helped us achieve several new top 10 keyword rankings on search and increase our organic traffic by over 100%. In addition, their PPC management has significantly lowered our cost per lead and increased lead volume. Prior to working with BrightPathWebGrowth, we tried several other Search vendors. BrightPathWebGrowth is the only one that was able to deliver results. I wouldn't hesitate to recommend BrightPathWebGrowth to anyone looking for professional, reliable, cost effective SEO and PPC services.</p>
  </div>
  <div class="testimonial abs" style="left:266px;top:880px">
    <h4>TOWNAHEAD.COM</h4><div class="who">Martin Ashby - Brand Manager</div>
    <p>Strategic Thinker, Master Executer, Dependable Manager. Ivan exemplifies the qualities one looks for in a person to run a marketing channel. He proactively addresses problems, allowing his attention to be focused (as it should be) on the goal. In the years I've managed search campaigns, there are very few to whom I would entrust my business. BrightPathWebGrowth is at the top of that list.</p>
  </div>

  <div class="case abs" style="left:515px;top:849px"><h4>PEAKDRIVE.COM</h4><ul><li>- Using our services for <b>2 months</b></li><li>- Increased revenue up to <b>200%</b></li><li>- Got more than <b>100 new customers</b></li></ul></div>
  <div class="photo abs" style="left:686px;top:845px;width:180px;height:124px;transform:rotate(-2deg)"><div role="img" aria-label="Group of smiling business people" style="background:linear-gradient(135deg,#6a6f7a,#2c3140 60%,#c9b9a8)"></div></div>
  <div class="photo abs" style="left:529px;top:930px;width:168px;height:126px;transform:rotate(2deg)"><div role="img" aria-label="Businessman standing in front of a suburban house" style="background:linear-gradient(#6fa3d8,#b9d3ea 55%,#7da04f 56%,#5c8a3a)"></div></div>
  <svg class="abs" style="left:640px;top:890px" width="110" height="110"><path class="leader" d="M14 18h12l14 9"/><path class="leader" d="M67 95h22l13 12"/></svg>
  <div class="case abs" style="left:720px;top:1003px"><h4>HOMEKIND.COM</h4><ul><li>- Using our services for <b>4 months</b></li><li>- Increased revenue up to <b>200%</b></li><li>- Got more than <b>10 sells a day</b></li></ul></div>

  <a class="btn-read abs">Read Other Testimonials</a>
  <div class="btn-read-mark abs"></div>
</section>

<footer class="site-footer abs">All rights reserved. Bright Path Web Growth, Copyright © 2012</footer>
</body>
</html>
```